Website overhaul! mvrcoatings.example

We need some life, professionalism and style put into our site... right now it’s basic and looking unprofessional! Help!

Currently 2 physical store locations that need showcasing and our online store requires easy navigation to categories divided by brand or product type.

80% of our sales are made up of paints for decorating your home, which we sell to the trade painter and end user.

Our company colours are grey and orange - as per our logo so theme based around this with some decent images that stand out.

Target Market(s)

Painter, Decorator, DIY

Industry/Entity Type

Home Improvement

Font styles to use
Sans Serif

Colors
f37122
f78f20

Requirements
Must have
• Clear branding, easy navigation, uncomplicated and clean.

```html
<!DOCTYPE html>
<html lang="en">
<head>
<meta charset="utf-8">
<title>MVR Coatings – Home</title>
<link href="https://fonts.googleapis.com/css2?family=Montserrat:wght@500;600;700;800&family=Open+Sans:wght@400;600;700&display=swap" rel="stylesheet">
<style>
:root{
  --orange:#f37122;
  --orange-2:#f78f20;
  --topbar:#1d6e9e;
  --ink:#1f2633;
  --text:#555b63;
  --muted:#8a8f96;
  --band:#eeeeee;
  --paper:#fafafa;
  --white:#ffffff;
  --navy:#2c3546;
  --card-grey:#5d646b;
  --line:#e3e3e3;
}
*{box-sizing:border-box;margin:0;padding:0}
html,body{width:1200px;height:3750px;overflow:hidden}
body{position:relative;background:var(--white);font-family:'Open Sans',sans-serif;color:var(--text)}
.abs{position:absolute}
.head{font-family:'Montserrat',sans-serif}

/* top bar + header */
.topbar{left:0;top:0;width:1200px;height:52px;background:var(--topbar);color:#fff;font-size:13px;text-align:center;line-height:52px}
.header{left:0;top:52px;width:1200px;height:68px;background:#fff;box-shadow:0 1px 4px rgba(0,0,0,.08)}
.brand{left:150px;top:6px;width:56px;display:flex;flex-direction:column;align-items:center;gap:2px}
.brand-dot{width:36px;height:36px;border-radius:50%;border:3px solid var(--orange)}
.brand-name{font-family:'Montserrat',sans-serif;font-weight:800;font-size:8.5px;color:var(--orange);line-height:1.1;white-space:nowrap}
.nav{left:233px;top:23px;font-family:'Montserrat',sans-serif;font-weight:600;font-size:14px;color:var(--ink)}
.nav a{text-decoration:none;color:inherit;position:absolute;white-space:nowrap}
.nav a.active{color:var(--orange)}
.search{left:476px;top:16px;width:400px;height:31px;border:1px solid #cfcfcf;border-radius:16px;display:flex;overflow:hidden;background:#fff}
.search-cat{width:110px;background:#f1f1f1;font-size:12px;color:#444;line-height:29px;padding-left:12px;border-right:1px solid #d5d5d5}
.search-input{flex:1;font-size:10px;font-style:italic;color:#aaa;line-height:29px;padding-left:8px}
.search-btn{width:40px;background:var(--orange);display:flex;align-items:center;justify-content:center}
.account{left:897px;top:18px;font-size:11px;color:var(--ink);line-height:1.3}
.account b{font-weight:700}
.cart{left:986px;top:25px;display:flex;align-items:center;gap:6px;font-size:11px;color:var(--ink)}

/* hero */
.hero{left:0;top:120px;width:1200px;height:646px;background:linear-gradient(180deg,#3c74b4 0%,#6c95c8 22%,#3e3b3a 40%,#2c2a29 62%,#8a5b42 74%,#8d887f 88%,#7a7468 100%)}
.hero-title{left:204px;top:215px;color:#fff;font-family:'Montserrat',sans-serif;font-weight:800;font-size:27px;line-height:41px;letter-spacing:.2px;text-transform:uppercase;text-shadow:0 2px 4px rgba(0,0,0,.4)}
.btn{display:flex;align-items:center;justify-content:center;font-family:'Montserrat',sans-serif;font-weight:700;text-transform:uppercase;border-radius:22px}
.btn-solid{background:var(--orange);color:#fff}
.btn-ghost{background:#fff;color:var(--orange);border:2px solid var(--orange)}
.hero .btn{top:413px;width:194px;height:41px;font-size:14px}
.dots{left:555px;top:622px;display:flex;gap:16px}
.dot{width:10px;height:10px;border-radius:50%;background:#fff}
.dot.on{background:transparent;border:3px solid var(--orange);box-shadow:0 0 0 2px #fff}

.band{left:0;width:1200px;background:var(--band)}

/* contact */
.contact{left:0;top:826px;width:1200px;height:288px;background:var(--paper)}
.section-title{font-family:'Montserrat',sans-serif;font-weight:700;font-size:29px;color:var(--ink);text-decoration:underline;text-underline-offset:5px;text-decoration-thickness:2px}
.contact-copy{left:151px;top:118px;width:390px;font-size:13px;line-height:18px;color:var(--text)}
.contact-col{font-size:13px;line-height:19px;color:var(--text)}
.contact-col b{color:var(--ink);font-weight:700}
.follow{left:877px;top:106px;font-family:'Montserrat',sans-serif;font-weight:600;font-size:13px;color:var(--ink)}
.social{display:flex;gap:20px}
.social span{width:14px;height:14px;border-radius:50%;background:#7c8590}

/* promo cards */
.promo{overflow:hidden;color:#fff}
.promo-art{position:absolute;inset:0}
.promo h3{position:absolute;left:18px;top:20px;font-family:'Montserrat',sans-serif;font-weight:700;font-size:18px;line-height:27px;z-index:1}
.promo p{position:absolute;left:18px;top:64px;font-size:13px;line-height:20px;width:220px;z-index:1}
.promo .btn{position:absolute;left:18px;top:165px;width:135px;height:36px;font-size:13px;z-index:1}

/* blog */
.blog-card{background:#fff;box-shadow:0 1px 5px rgba(0,0,0,.13);height:463px;width:292px}
.blog-img{position:absolute;left:0;top:0;width:100%;height:218px}
.blog-stats{position:absolute;left:0;top:100px;width:100%;display:flex;justify-content:center;align-items:center;gap:10px;color:#fff;font-size:10px}
.blog-stats i{display:inline-block;width:10px;height:8px;background:#fff;border-radius:5px;margin-right:5px;vertical-align:-1px}
.blog-stats .sep{width:1px;height:14px;background:#fff}
.blog-card h4{position:absolute;left:15px;top:240px;font-family:'Montserrat',sans-serif;font-weight:700;font-size:13px;color:var(--ink)}
.blog-card .excerpt{position:absolute;left:15px;top:270px;width:265px;font-size:12.5px;line-height:15px;color:var(--muted)}
.author{position:absolute;left:15px;top:379px;display:flex;align-items:center;gap:8px;font-family:'Montserrat',sans-serif;font-weight:600;font-size:12px;color:var(--ink)}
.avatar{width:22px;height:22px;border-radius:50%;background:#6f6a66}
.author small{font-family:'Open Sans',sans-serif;font-weight:400;font-size:9.5px;color:var(--muted);margin-left:8px}
.read{position:absolute;left:0;width:100%;top:433px;text-align:center;font-family:'Montserrat',sans-serif;font-weight:700;font-size:12.5px;color:var(--ink)}

/* feed */
.tweet{background:#fff;box-shadow:0 1px 5px rgba(0,0,0,.12);width:288px;height:339px;font-size:11.5px;line-height:14px;color:#333}
.tweet-head{position:absolute;left:16px;top:10px;display:flex;gap:8px;align-items:flex-start}
.tweet-av{width:26px;height:26px;border-radius:50%;background:#fff;border:2px solid #d9d9d9}
.tweet-av.dark{background:#2a2a2a;border-color:#c9a227}
.tweet-name{font-family:'Montserrat',sans-serif;font-weight:700;font-size:12.5px;color:var(--ink);line-height:15px}
.tweet-handle{font-size:11.5px;color:#666}
.tweet-body{position:absolute;left:18px;top:50px;width:258px}
.tweet-body .tag{color:var(--orange-2)}
.tweet-img{position:absolute;left:19px;top:135px;width:208px;height:134px;border-radius:4px}
.tweet-meta{position:absolute;left:18px;top:281px;font-size:9px;color:#666;line-height:12px}
.tweet-meta b{color:#333}
.tweet-actions{position:absolute;left:18px;top:317px;display:flex;gap:22px;font-size:8px;color:#999;align-items:center}
.tweet-actions i{display:inline-block;width:8px;height:7px;border:1px solid #aaa;border-radius:3px;margin-right:3px;vertical-align:-1px}

/* mailing */
.mailing{left:0;top:3148px;width:1200px;height:431px;background:#fff}
.field{border:1px solid #cfcfcf;border-radius:20px;height:38px;font-size:13px;color:#777;line-height:36px;padding-left:12px;width:198px}

/* footer */
.footer{left:0;top:3579px;width:1200px;height:171px;background:linear-gradient(115deg,#27303f 0%,#2f3a4c 60%,#28313f 100%);color:#fff}
.footer h5{font-family:'Montserrat',sans-serif;font-weight:700;font-size:11.5px;letter-spacing:.3px;text-transform:uppercase}
.footer ul{list-style:none;font-size:12px;line-height:23px;color:#e0e3e8}
.pay{display:flex;gap:10px}
.pay span{width:24px;height:15px;border-radius:2px;background:#cfd6df}
</style>
</head>
<body>

<div class="abs topbar">All stores are OPEN 7.00am-5.00pm Monday to Friday &amp; 8.00am-12.00pm Saturdays / Closed Sundays</div>

<header class="abs header">
  <div class="abs brand">
    <span class="brand-dot"></span>
    <span class="brand-name">MVR COATINGS</span>
  </div>
  <nav class="abs nav">
    <a class="active" style="left:0">Home</a>
    <a style="left:79px">Contact Us</a>
    <a style="left:189px">Shop</a>
  </nav>
  <div class="abs search">
    <div class="search-cat">All Categories ▾</div>
    <div class="search-input">Discover something...</div>
    <div class="search-btn">
      <svg width="16" height="16" viewBox="0 0 16 16"><circle cx="9" cy="7" r="5" fill="none" stroke="#fff" stroke-width="2"/><line x1="5.5" y1="10.5" x2="2" y2="14" stroke="#fff" stroke-width="2"/></svg>
    </div>
  </div>
  <div class="abs account">Hello, Log in<br><b>My account</b></div>
  <div class="abs cart">
    <svg width="18" height="16" viewBox="0 0 18 16"><path d="M1 1h3l2 9h9l2-6H5" fill="none" stroke="#1f2633" stroke-width="1.5"/><circle cx="7" cy="13.5" r="1.5" fill="#1f2633"/><circle cx="14" cy="13.5" r="1.5" fill="#1f2633"/></svg>
    <span>My Cart</span>
  </div>
</header>

<section class="abs hero" role="img" aria-label="Photograph of a timber-clad barn house painted black with brick base under a blue sky">
  <svg class="abs" style="left:30px;top:296px" width="30" height="54" viewBox="0 0 30 54"><polyline points="26,2 4,27 26,52" fill="none" stroke="#e0761f" stroke-width="3"/></svg>
  <svg class="abs" style="left:1140px;top:296px" width="30" height="54" viewBox="0 0 30 54"><polyline points="4,2 26,27 4,52" fill="none" stroke="#e0761f" stroke-width="3"/></svg>
  <h1 class="abs hero-title">Outstanding quality water-based paint<br>multi-surface and barn paint</h1>
  <a class="abs btn btn-solid" style="left:211px">Shop now</a>
  <a class="abs btn btn-ghost" style="left:421px">Visit blog</a>
  <div class="abs dots"><span class="dot"></span><span class="dot on"></span><span class="dot"></span><span class="dot"></span></div>
</section>

<div class="abs band" style="top:766px;height:60px"></div>

<section class="abs contact">
  <h2 class="abs section-title" style="left:151px;top:63px">Contact us</h2>
  <p class="abs contact-copy">Lorem ipsum dolor sit amet, consectetur adipisicing elit, sed do eiusmod tempor incididunt ut labore et dolore magna aliqua. Ut enim ad minim veniam, quis nostrud exercitation ullamco laboris nisi ut aliquip ex ea commodo consequat.</p>
  <div class="abs contact-col" style="left:606px;top:116px">14 Mill Lane,<br>Eastfield EF2 4HL, United Kingdom</div>
  <div class="abs contact-col" style="left:606px;top:165px">northbrook@mvrcoatings.example</div>
  <div class="abs contact-col" style="left:606px;top:192px"><b>Northbrook</b><br><span style="display:block;margin-top:7px">01632 960877</span></div>
  <div class="abs contact-col" style="left:743px;top:192px"><b>Eastfield</b><br><span style="display:block;margin-top:7px">01632 960213</span></div>
  <div class="abs follow">Follow us</div>
  <div class="abs social" style="left:878px;top:134px"><span style="background:#2a5ea8"></span><span></span><span></span><span></span></div>
</section>

<div class="abs band" style="top:1114px;height:36px"></div>

<section class="abs" style="left:0;top:1150px;width:1200px;height:753px;background:#fff">
  <article class="abs promo" style="left:150px;top:21px;width:443px;height:220px">
    <div class="promo-art" role="img" aria-label="Box of disposable face masks on a dark starry background" style="background:linear-gradient(135deg,#14202e 0%,#1c2b3d 55%,#2a3c52 100%)"></div>
    <div class="abs" role="img" aria-label="Face mask box" style="left:252px;top:50px;width:178px;height:140px;background:linear-gradient(160deg,#f4f6f8,#cfd6dc);border-radius:6px;transform:skewY(-10deg)"></div>
    <h3>Diposable&nbsp; Face Masks</h3>
    <p style="width:215px">Each box contains 50 Masks and shipping&nbsp; is free for you<br>buy 3 boxes or more</p>
    <a class="btn btn-solid">Shop now</a>
  </article>
  <article class="abs promo" style="left:607px;top:21px;width:444px;height:220px">
    <div class="promo-art" role="img" aria-label="Navy painted cabinet with art deco panel detail" style="background:linear-gradient(90deg,#22384d 0%,#2d4a63 50%,#253e55 100%)"></div>
    <h3>Protect Your Painted Furniture</h3>
    <p style="width:260px">With Sheenguard Decoratore Varnish</p>
    <a class="btn btn-solid">Shop now</a>
  </article>
  <article class="abs promo" style="left:150px;top:262px;width:443px;height:222px">
    <div class="promo-art" role="img" aria-label="Yellow front door in a grey stone doorway" style="background:linear-gradient(90deg,#5c6267 0%,#63686c 55%,#8f8a5a 78%,#5a5e60 100%)"></div>
    <h3>Front Door Makeover</h3>
    <p style="width:225px">from bghit yellow to rich maroon, make a statement with your front door</p>
    <a class="btn btn-ghost" style="color:var(--ink);border-color:#fff">Visit blog</a>
  </article>
  <article class="abs promo" style="left:607px;top:262px;width:444px;height:222px">
    <div class="promo-art" style="background:var(--card-grey)"></div>
    <div class="abs" role="img" aria-label="Colourful kitchen wall paint guide cover" style="left:280px;top:32px;width:160px;height:157px;background:linear-gradient(135deg,#f2c94c,#e9a03b 45%,#4aa3a0 75%,#2d3640)"></div>
    <h3 style="width:260px">Our Guide to kitchen wall Paint</h3>
    <a class="btn btn-ghost" style="color:var(--ink);border-color:#fff">Visit blog</a>
  </article>
  <article class="abs promo" style="left:150px;top:507px;width:900px;height:221px">
    <div class="promo-art" role="img" aria-label="Long-exposure light trails over a grey background" style="background:radial-gradient(ellipse at 70% 40%,#8a8a8a 0%,#6e6e6e 45%,#5d5d5d 100%)"></div>
    <div class="abs" style="left:594px;top:14px;width:192px;height:192px;border-radius:50%;background:#2b2d2f;border:6px solid #4a4c4e"></div>
    <h3 style="left:84px;top:38px;font-size:28px;color:var(--orange-2)">Eco Friendly Paint</h3>
    <p style="left:85px;top:92px;width:320px;font-family:'Montserrat',sans-serif;font-weight:500;font-size:17px;line-height:27px">Eco-friendly paint formulas and recyclable materials</p>
  </article>
</section>

<div class="abs band" style="top:1903px;height:57px"></div>

<section class="abs" style="left:0;top:1960px;width:1200px;height:639px;background:#fff">
  <h2 class="section-title" style="position:absolute;left:0;width:1216px;top:20px;text-align:center">Blog Posts</h2>

  <article class="abs blog-card" style="left:143px;top:78px">
    <div class="blog-img" role="img" aria-label="Kitchen wall paint guide cover, dimmed" style="background:linear-gradient(135deg,#9b8a5a,#6f6a58 50%,#4c5560)"></div>
    <div class="blog-stats"><span><i></i>966</span><span class="sep"></span><span><i></i>5683</span></div>
    <h4>Our Guide To Kitchen Wall Paint</h4>
    <p class="excerpt">Our guide to kitchen wall paint From spag bowl sauce splatters to chip pan grease, kitchen walls can be a hotbed for stains and scuffs. Here’s our guide to the best paints for your kitchen walls to make sure they’re......</p>
    <div class="author"><span class="avatar"></span>Owen Carter<small>October 14, 2020</small></div>
    <div class="read">Read now ›</div>
  </article>

  <article class="abs blog-card" style="left:451px;top:78px">
    <div class="blog-img" role="img" aria-label="Dark circular paint brand badge on a grey green backdrop" style="background:radial-gradient(circle at 50% 50%,#2b2e2c 0%,#2f3431 45%,#55605a 100%)"></div>
    <div class="blog-stats"><span><i></i>695</span><span class="sep"></span><span><i></i>236</span></div>
    <h4>Harrow And Vale Launching Soon...!</h4>
    <p class="excerpt">We will soon be launching Harrow and Vale paint on our website shop with special introductory offers. Stay tuned for the launch date...</p>
    <div class="author"><span class="avatar"></span>Rhys Dalton<small>August 27, 2020</small></div>
    <div class="read">Read now ›</div>
  </article>

  <article class="abs blog-card" style="left:759px;top:78px">
    <div class="blog-img" role="img" aria-label="Row of terraced houses with colourful front doors at dusk" style="background:linear-gradient(180deg,#3b3633 0%,#2f2b2a 55%,#4a3a34 100%)"></div>
    <div class="blog-stats"><span><i></i>236</span><span class="sep"></span><span><i></i>659</span></div>
    <h4>Front Door Makeover</h4>
    <p class="excerpt">Everyone seems to be making a statement with their choice of front door colour at the moment. From rich maroons and dark greens to vibrant yellows and pops of pink your front door can give an impactful first impression of...</p>
    <div class="author"><span class="avatar"></span>Rhys Dalton<small>August 27, 2020</small></div>
    <div class="read">Read now ›</div>
  </article>

  <a class="abs btn btn-solid" style="left:498px;top:581px;width:197px;height:39px;font-size:13px;text-transform:none;box-shadow:0 3px 6px rgba(0,0,0,.15)">See More ›</a>
</section>

<div class="abs band" style="top:2599px;height:44px"></div>

<section class="abs" style="left:0;top:2643px;width:1200px;height:465px;background:#fff">
  <h2 class="section-title" style="position:absolute;left:0;width:1200px;top:28px;text-align:center">Chirper Feed</h2>

  <article class="abs tweet" style="left:153px;top:83px">
    <div class="tweet-head"><span class="tweet-av dark"></span><div><div class="tweet-name">CALDER DECORATORS LTD</div><div class="tweet-handle">@CalderDecor</div></div></div>
    <div class="tweet-body">This was a stair and hall we painted with <span class="tag">@Stonecroft</span>Trade paints, colour matched to Harrow &amp; Vale “Misty Grey”.<br><span class="tag" style="display:block;margin-top:4px">#painting #painters #colours #Edinburgh #Perth #Stirling #Crieff</span></div>
    <div class="tweet-img" style="top:136px;background:linear-gradient(90deg,#7d8fa3 0%,#a88e6d 40%,#c9b79d 70%,#8d6f52 100%)" role="img" aria-label="Painted hallway with staircase and wooden doors"></div>
    <div class="tweet-meta">Oct 28, 2020<br><br><b>1</b> Retweet &nbsp; <b>11</b> Likes</div>
    <div class="tweet-actions"><span><i></i>1</span><span><i></i>1</span><span><i></i>11</span><span><i></i></span></div>
  </article>

  <article class="abs tweet" style="left:460px;top:83px">
    <div class="tweet-head"><span class="tweet-av"></span><div><div class="tweet-name">MVR COATINGS</div><div class="tweet-handle">@MVRcoatings</div></div></div>
    <div class="tweet-body">We’re running weekly quizzes on our Pictura stories. Have a go at testing yourknowledge and be in with a chance of winning a free T-shirt!<br><span style="display:block;margin-top:4px">What future quiz topics would you like to see? <span class="tag">#picturastoriesquiz #freetshirt</span></span></div>
    <div class="tweet-img" style="top:136px;background:#2e2e2e" role="img" aria-label="Promotional graphic asking about story quizzes"></div>
    <div class="tweet-meta">Oct 22, 2020<br><br><b>1</b> Retweet &nbsp; <b>11</b> Likes</div>
    <div class="tweet-actions"><span><i></i>1</span><span><i></i>1</span><span><i></i>11</span><span><i></i></span></div>
  </article>

  <article class="abs tweet" style="left:763px;top:83px">
    <div class="tweet-head"><span class="tweet-av"></span><div><div class="tweet-name">MVR COATINGS</div><div class="tweet-handle">@MVRcoatings</div></div></div>
    <div class="tweet-body">Fascia repair by @brushwork_ben using <span class="tag">@Fillmaster</span> wood filler supplied by us.<br><span style="display:block;margin-top:14px">What have you used this product on? <span class="tag">#fillmasterfillers #fillmasterwoodfiller</span></span></div>
    <div class="tweet-img" style="top:136px;background:linear-gradient(90deg,#b8555a 0%,#a84a4e 55%,#6f7f99 80%,#9fb3cc 100%)" role="img" aria-label="Repaired red scalloped fascia board against the sky"></div>
    <div class="tweet-meta">Oct 22, 2020<br><br><b>1</b> Retweet &nbsp; <b>11</b> Likes</div>
    <div class="tweet-actions"><span><i></i>1</span><span><i></i>1</span><span><i></i>11</span><span><i></i></span></div>
  </article>
</section>

<div class="abs band" style="top:3108px;height:40px"></div>

<section class="abs mailing">
  <h2 class="head" style="position:absolute;left:0;width:1218px;top:30px;text-align:center;font-weight:600;font-size:29px;color:var(--ink)">Mailing List</h2>
  <svg class="abs" style="left:563px;top:76px" width="74" height="74" viewBox="0 0 74 74"><circle cx="37" cy="37" r="37" fill="#f37122"/><rect x="19" y="25" width="36" height="25" fill="none" stroke="#fff" stroke-width="2.5"/><polyline points="19,25 37,40 55,25" fill="none" stroke="#fff" stroke-width="2.5"/></svg>
  <h3 class="head" style="position:absolute;left:0;width:1200px;top:164px;text-align:center;font-weight:700;font-size:30px;color:var(--orange-2)">Subscribe to our newsletter</h3>
  <p style="position:absolute;left:0;width:1200px;top:207px;text-align:center;font-size:12px;color:#333">Subscribe to our mailing list for all our latest offers and ideas.</p>
  <div class="abs field" style="left:396px;top:255px">Name</div>
  <div class="abs field" style="left:607px;top:255px">email address</div>
  <div class="abs" style="left:400px;top:325px;display:flex;align-items:center;gap:9px;font-size:12px;color:#333">
    <svg width="14" height="14" viewBox="0 0 14 14"><rect x="0.5" y="0.5" width="13" height="13" rx="2" fill="#fff" stroke="#ccc"/><polyline points="3,7 6,10 11,4" fill="none" stroke="#f37122" stroke-width="1.8"/></svg>
    Send me Weekly Newsletter
  </div>
  <a class="abs btn btn-solid" style="left:609px;top:316px;width:196px;height:37px;font-size:17px;text-transform:none;box-shadow:0 3px 6px rgba(0,0,0,.15)">Sign Up</a>
</section>

<footer class="abs footer">
  <div class="abs" style="left:162px;top:34px;display:flex;flex-direction:column;align-items:center;gap:4px">
    <span style="width:46px;height:46px;border-radius:50%;border:3px solid var(--orange)"></span>
    <span class="head" style="font-weight:800;font-size:13px;color:var(--orange)">MVR COATINGS</span>
  </div>
  <div class="abs" style="left:298px;top:42px">
    <h5>About us</h5>
    <ul style="margin-top:2px"><li>What We do</li><li>FAQ</li></ul>
  </div>
  <div class="abs" style="left:448px;top:42px">
    <h5>Main Menu</h5>
    <ul style="margin-top:2px"><li>Home</li><li>Contact Us</li><li>Shop</li></ul>
  </div>
  <div class="abs" style="left:981px;top:42px">
    <h5 style="text-transform:none">Follow us</h5>
  </div>
  <div class="abs social" style="left:982px;top:64px;gap:22px"><span style="background:#aab2bd"></span><span style="background:#aab2bd"></span><span style="background:#aab2bd"></span></div>
  <div class="abs pay" style="left:899px;top:107px"><span></span><span></span><span style="background:#f0a23a"></span><span></span><span style="background:#3d5bb5"></span></div>
  <p class="head" style="position:absolute;left:0;width:1200px;top:148px;text-align:center;font-size:12.5px;font-weight:500;color:#fff">Copyright © 2020 MVR Coatings Ltd.</p>
</footer>

</body>
</html>
```